Form With Tamsin - Health and Wellness Business Card and Logo

I need a business card design with a logo for my business you can check out at www.formwithtamsin.net. I want something more original, simplistic, and memorable than the basic logo I have on my site currently. I am a health and wellness coach and I offer mindset coaching and nutrition plans. I like the colour teal and dark grey/black for my theme colours. I emphasize growth, longterm change, and the whole package of "healthy mind, healthy body, healthy life". I had played around the idea of intertwining 3 T's or incorporating growth (leaves etc.) into my design. I want my expertise and experience to show through. In one glance I want people to understand with confidence I can help them accomplish anything they set their minds to. I look forward to seeing what everyone comes up with!

Industry/Entity Type

Health And Wellness

Contact Information for Business Card

Form With Tamsin
Tamsin Arlow
BSc, Health & Wellness Coach
"Manifest your best"
www.formwithtamsin.net
formwithtamsin@mailo.example
613-472-9186
[Instagram logo] @tamsinarlow

Colors
33b8a4
ffffff
333333
000000

Requirements
Must have
• A memorable and unique logo for my business!
Nice to have
• Could have the phrase "Are you unhappy with your body and state of health?" or "It takes the right skills to develop habits in order to create long term change. I can help you get there."

```html
<!DOCTYPE html>
<html lang="en">
<head>
<meta charset="UTF-8">
<title>Form With Tamsin – Business Card</title>
<link rel="stylesheet" href="https://fonts.googleapis.com/css2?family=Montserrat:wght@300&family=Tinos&display=swap">
<style>
  :root {
    --teal: #33a9a6;
    --white: #ffffff;
    --ink: #555555;
    --backdrop: #3b3b3b;
    --card-shadow: rgba(0, 0, 0, 0.35);
  }
  * { box-sizing: border-box; margin: 0; padding: 0; }
  html, body {
    width: 1200px;
    height: 900px;
    overflow: hidden;
    background: var(--backdrop);
  }
  .stage {
    position: relative;
    width: 1200px;
    height: 900px;
  }
  .card {
    position: absolute;
    width: 600px;
    height: 343px;
    border-radius: 22px;
    box-shadow: 0 14px 30px var(--card-shadow);
    display: flex;
    flex-direction: column;
    align-items: center;
  }
  .card--back {
    top: 70px;
    left: 520px;
    background: var(--teal);
    justify-content: center;
  }
  .card--front {
    top: 470px;
    left: 80px;
    background: var(--white);
    padding-top: 52px;
  }
  .brand {
    display: flex;
    align-items: center;
    gap: 14px;
    font-family: "Montserrat", sans-serif;
    font-weight: 300;
    letter-spacing: 0.08em;
    text-transform: uppercase;
  }
  .brand__dot {
    width: 22px;
    height: 22px;
    border-radius: 50%;
  }
  .card--back .brand { color: var(--white); font-size: 34px; }
  .card--back .brand__dot { background: var(--white); }
  .card--front .brand { color: var(--teal); font-size: 32px; }
  .card--front .brand__dot { background: var(--teal); }
  .contact {
    margin-top: 30px;
    text-align: center;
    font-family: "Tinos", serif;
    color: var(--ink);
    line-height: 1.3;
  }
  .contact__name {
    font-size: 26px;
    letter-spacing: 0.04em;
    text-transform: uppercase;
  }
  .contact__role {
    font-size: 15px;
    letter-spacing: 0.02em;
    text-transform: uppercase;
  }
  .contact__line { font-size: 17px; }
</style>
</head>
<body>
  <main class="stage">
    <section class="card card--back" aria-label="Card back">
      <div class="brand"><span class="brand__dot"></span>Form With Tamsin</div>
    </section>

    <section class="card card--front" aria-label="Card front">
      <div class="brand"><span class="brand__dot"></span>Form With Tamsin</div>
      <div class="contact">
        <p class="contact__name">Tamsin Arlow</p>
        <p class="contact__role">BSc, Health &amp; Wellness Coach, Trainer</p>
        <p class="contact__line">formwithtamsin@mailo.example | www.formwithtamsin.net</p>
        <p class="contact__line">004-555-0187</p>
      </div>
    </section>
  </main>
</body>
</html>
```